3 x DIN A4 Flyer, Vorder- und Rückseite
Zielgruppe
Handwerksunternehmen
Aufgabenstellung
Wir benötigen 3 Werbeflyer die in Zeitschriften beigelegt werden. Jeweils DIN A4, Vorderseite beschreibt das Produkt, Rückseite kann zur Bestellung mittels Faxantwort benutzt werden. Profibilder und Text wird vollständig geliefert.

```html
<!DOCTYPE html>
<html lang="de">
<head>
<meta charset="utf-8">
<title>Flyer Kundenstopper und Baustellen-Handy</title>
<link href="https://fonts.googleapis.com/css2?family=PT+Sans:wght@400;700&display=swap" rel="stylesheet">
<style>
:root{
  --page-bg:#e9edf1;
  --sky-top:#c9e3f5;
  --sky-bottom:#e6f2fb;
  --navy:#1f4f8f;
  --orange:#f08a00;
  --text:#2a3550;
  --box:rgba(255,255,255,.72);
  --price-bg:#ffffff;
  --photo-blue:#8fb6d3;
}
*{box-sizing:border-box;margin:0;padding:0}
html,body{width:1200px;height:800px;overflow:hidden;background:var(--page-bg);font-family:"PT Sans",Arial,sans-serif;color:var(--text)}
.canvas{position:relative;width:1200px;height:800px}
.flyer{position:absolute;top:30px;width:524px;height:740px;overflow:hidden;
  background:linear-gradient(180deg,var(--sky-top) 0%,var(--sky-bottom) 55%,var(--sky-top) 100%);
  box-shadow:0 4px 14px rgba(0,0,0,.18)}
.flyer--stand{left:46px}
.flyer--phone{left:630px}
.title-band{position:absolute;left:0;width:100%}
.title{position:absolute;font-weight:700;color:var(--navy);font-size:33px;letter-spacing:-.3px}
.subtitle{position:absolute;font-weight:700;color:var(--orange);line-height:1.15;text-align:right}
.photo{position:absolute;border-radius:4px}
.info-box{position:absolute;background:var(--box);border-radius:6px}
.arrow-list{list-style:none}
.arrow-list li{position:relative;padding-left:34px}
.arrow-list li svg{position:absolute;left:0;top:50%;transform:translateY(-50%)}
.price{position:absolute;background:var(--price-bg);border-radius:4px;color:var(--navy);font-weight:700;display:flex;align-items:baseline;gap:6px;box-shadow:0 1px 4px rgba(0,0,0,.15)}
.price__amount{font-size:28px}
.price__unit{font-size:11px;line-height:1}
.price__unit small{display:block;font-size:7px;font-weight:400}
.plus-list{list-style:none;font-size:9px;line-height:1.3}
.plus-list li{position:relative;padding-left:12px;margin-bottom:2px}
.plus-list li::before{content:"+";position:absolute;left:0;color:var(--navy);font-weight:700}
.plus-list b{color:var(--navy)}
.legal{position:absolute;left:0;width:100%;text-align:center;font-size:7.5px;line-height:1.45}
.imprint{position:absolute;left:0;width:100%;text-align:center;font-size:7.5px}
.body-copy{position:absolute;font-size:8.4px;line-height:1.35}
.body-copy .arrow-list li{padding-left:22px;margin-bottom:8px}
.feature-box{position:absolute;left:18px;top:500px;width:340px;height:170px;background:var(--box);border-radius:6px;padding:10px 10px;display:flex;gap:10px}
.feature-box .plus-list{flex:1;font-size:7.6px;line-height:1.25}
</style>
</head>
<body>
<div class="canvas">

  <!-- Flyer 1: Kundenstopper -->
  <section class="flyer flyer--stand">
    <svg class="title-band" style="top:72px" width="524" height="70" viewBox="0 0 524 70">
      <path d="M0 18 Q260 -6 524 10 L524 56 Q260 40 0 64 Z" fill="#ffffff" opacity=".9"/>
    </svg>
    <h1 class="title" style="left:42px;top:82px">Kundenstopper</h1>
    <p class="subtitle" style="right:22px;top:140px;font-size:26px">clever werben<br>auf der Baustelle!</p>

    <div class="photo" role="img" aria-label="Foto eines silbernen Kundenstoppers mit Klapprahmen" style="left:30px;top:210px;width:240px;height:330px;background:linear-gradient(160deg,#e3e8ee,#9aa7b4)"></div>
    <p style="position:absolute;left:110px;top:330px;font-size:9.5px;font-weight:700;line-height:1.4;color:#243049">Plakatformat!<br>DIN A1 (60cm x 85cm)<br><br>Ständermaße! (121cm x 66cm)</p>

    <div class="info-box" style="left:260px;top:250px;width:246px;height:215px;padding:14px 16px">
      <p style="font-size:9.5px;font-weight:700;line-height:1.5;margin-bottom:12px">Kundenstopper / Werbeständer /<br>Gehwegaufsteller / Bockständer<br>für Innen und Außen!</p>
      <ul class="arrow-list" style="font-size:12.5px;line-height:2.05">
        <li><svg width="14" height="10" viewBox="0 0 14 10"><path d="M0 5H12M8 1L12 5L8 9" stroke="var(--navy)" stroke-width="1.6" fill="none"/></svg>Messen</li>
        <li><svg width="14" height="10" viewBox="0 0 14 10"><path d="M0 5H12M8 1L12 5L8 9" stroke="var(--navy)" stroke-width="1.6" fill="none"/></svg>Aktionstage</li>
        <li><svg width="14" height="10" viewBox="0 0 14 10"><path d="M0 5H12M8 1L12 5L8 9" stroke="var(--navy)" stroke-width="1.6" fill="none"/></svg>Tag der offenen Tür</li>
        <li><svg width="14" height="10" viewBox="0 0 14 10"><path d="M0 5H12M8 1L12 5L8 9" stroke="var(--navy)" stroke-width="1.6" fill="none"/></svg>Gewerbeveranstaltungen</li>
        <li><svg width="14" height="10" viewBox="0 0 14 10"><path d="M0 5H12M8 1L12 5L8 9" stroke="var(--navy)" stroke-width="1.6" fill="none"/></svg>vor dem Betrieb</li>
      </ul>
    </div>

    <div class="price" style="left:36px;top:532px;padding:6px 28px 6px 34px">
      <span class="price__amount">39,–</span><span class="price__unit">EUR*<small>(netto)</small></span>
    </div>

    <div style="position:absolute;left:170px;top:590px;width:320px">
      <p style="font-size:9.5px;font-weight:700;color:var(--navy);margin-bottom:8px">Produktdetails</p>
      <ul class="plus-list">
        <li>klappbares Standgestell</li>
        <li>2 aufmontierte Klemmrahmen mit 32 mm breitem Profil mit übergroßer Antireflex-Schutzfolie</li>
        <li>Ecken auf Gehrung geschnitten</li>
        <li>verzinkte Stahlblechrückwand (einseitig beschichtet) und Antireflex-Schutzfolie</li>
        <li>beidseitig nutzbar</li>
      </ul>
    </div>

    <p class="legal" style="top:690px">* Alle angegebenen Preise verstehen sich in Euro zzgl. der gesetzlichen geltenden Mehrwertsteuer von derzeit 19%.<br>Die Lieferung erfolgt ca.10 Tage nach Bestelleingang. Porto/Verpackung 12,90 Euro</p>
    <p class="imprint" style="top:720px">Fördergesellschaft Klever Technik mbH · Lindenweg 12 · 80331 München · www.klvt.de</p>
  </section>

  <!-- Flyer 2: Baustellen-Handy -->
  <section class="flyer flyer--phone">
    <svg class="title-band" style="top:22px" width="524" height="90" viewBox="0 0 524 90">
      <path d="M0 10 Q260 -4 524 14 L524 70 Q260 52 0 80 Z" fill="#ffffff" opacity=".9"/>
    </svg>
    <h1 class="title" style="left:20px;top:36px;font-size:35px">Baustellen-Handy</h1>
    <p class="subtitle" style="right:18px;top:92px;font-size:26px">mit Solar-Betrieb</p>

    <div class="photo" role="img" aria-label="Foto eines gelb-schwarzen robusten Outdoor-Handys" style="left:28px;top:148px;width:150px;height:300px;border-radius:22px;background:linear-gradient(180deg,#f1e11a 0%,#3a3a3a 40%,#222 100%)"></div>

    <div class="price" style="left:20px;top:350px;padding:6px 18px 6px 14px">
      <span class="price__amount">120,–</span><span class="price__unit">EUR*<small>(netto)</small></span>
    </div>

    <div class="body-copy" style="left:184px;top:148px;width:325px">
      <ul class="arrow-list">
        <li><svg width="12" height="9" viewBox="0 0 14 10"><path d="M0 5H12M8 1L12 5L8 9" stroke="var(--navy)" stroke-width="1.6" fill="none"/></svg>Übersteht dank abnehmbarem &amp; nachleuchtendem Shock Guard Stürze aus 2 Meter</li>
        <li><svg width="12" height="9" viewBox="0 0 14 10"><path d="M0 5H12M8 1L12 5L8 9" stroke="var(--navy)" stroke-width="1.6" fill="none"/></svg>Das geniale Baustellen-Handy für Handwerker, die Freiheit und Unabhängigkeit lieben. Die Freiheit, nicht mehr länger auf Ihr Handy aufpassen zu müssen. Und die Unabhängigkeit von einer anderen Stromquelle als der Sonne.</li>
        <li><svg width="12" height="9" viewBox="0 0 14 10"><path d="M0 5H12M8 1L12 5L8 9" stroke="var(--navy)" stroke-width="1.6" fill="none"/></svg>In seinem nachleuchtenden Shock Guard übersteht das RX-40 SUN sogar einen Sturz aus 2 Meter Höhe.</li>
        <li><svg width="12" height="9" viewBox="0 0 14 10"><path d="M0 5H12M8 1L12 5L8 9" stroke="var(--navy)" stroke-width="1.6" fill="none"/></svg>Dank Schutzklasse IP67 lässt es sich auch von Regen oder kurzzeitigem Untertauchen nicht beeindrucken. Das ideale Handy für alle, die viel im Freien arbeiten oder unterwegs sind, z.B. auf der Baustelle, in den Bergen, auf dem Boot oder beim Abenteuer-Urlaub.</li>
        <li><svg width="12" height="9" viewBox="0 0 14 10"><path d="M0 5H12M8 1L12 5L8 9" stroke="var(--navy)" stroke-width="1.6" fill="none"/></svg>Genießen Sie Unabhängigkeit: Der Akku hat eine Standby-Zeit von über einer Woche. Sobald Ihr RX-40 ans Tageslicht kommt, tankt es über seine Solarzelle neue Energie.</li>
        <li><svg width="12" height="9" viewBox="0 0 14 10"><path d="M0 5H12M8 1L12 5L8 9" stroke="var(--navy)" stroke-width="1.6" fill="none"/></svg>Auch genial: Der phosphoreszierende Shock Guard. Damit geht Ihr neues Action-Handy auch im Dunkeln nicht verloren.</li>
        <li><svg width="12" height="9" viewBox="0 0 14 10"><path d="M0 5H12M8 1L12 5L8 9" stroke="var(--navy)" stroke-width="1.6" fill="none"/></svg>Technik pur ohne Schnickschnack: Das RX-40 SUN bietet genau das, was Sie im Alltag brauchen. Bequemes Telefonieren und schnelles SMS-Schreiben.</li>
        <li><svg width="12" height="9" viewBox="0 0 14 10"><path d="M0 5H12M8 1L12 5L8 9" stroke="var(--navy)" stroke-width="1.6" fill="none"/></svg>Und wenn es in die Zivilisation zurückkehrt, wird das Handy auf Wunsch zum Normalo: Der Protector lässt sich einfach abnehmen.</li>
      </ul>
    </div>

    <div class="feature-box">
      <ul class="plus-list">
        <li><b>Startklar</b> Vertrags- und SIM-Lock-frei, sofort bereit für Ihre SIM-Karte</li>
        <li><b>Unverwüstlich</b> Stoßfestes sowie staub- und wasserdichtes Gehäuse (Schutzklasse IP67)</li>
        <li><b>Unabhängig &amp; umweltfreundlich</b> Integrierte Solarzelle auf der Rückseite</li>
        <li><b>Nachtaktiv</b> Phosphoreszierender Shock Guard (Schutz-Case), hintergrund­beleuchtetes Tastenfeld</li>
        <li><b>Verwandlungskünstler</b> Shock Guard aus Hartplastik lässt sich abnehmen</li>
        <li><b>Überall praktisch</b> UKW-Radio, LED-Taschenlampe, Spiele, Rechner, Wecker</li>
      </ul>
      <ul class="plus-list">
        <li><b>Kontraststark</b> 3,6 cm/1,8" Farb-TFT-Display, hintergrund-beleuchtet</li>
        <li><b>Klangfreudig</b> Polyphone Klingeltöne (16-stimmig), Vibrationsalarm</li>
        <li><b>Kontaktfreudig</b> SMS-Messaging, Telefonbuch (100 Einträge)</li>
        <li><b>Zuverlässig</b> Li-Ion-Akku 1000 mAh für 200 Min. Sprechen und 200 Std. Standby (lädt per Solar/ Netzteil)</li>
        <li><b>Handlich</b> Maße mit Hülle 108 x 48,5 x 18,5 mm</li>
        <li><b>Komplett</b> Inkl. Akku, 230V-Ladegerät, Ohrhörer, deutsches Handbuch</li>
      </ul>
    </div>

    <div class="photo" role="img" aria-label="Foto des Handys mit Solarzelle auf Kieselsteinen" style="left:370px;top:470px;width:138px;height:92px;background:linear-gradient(135deg,#c9b58c,#6f6a5e)"></div>
    <div class="photo" role="img" aria-label="Foto einer Hand, die das gelbe Handy hält" style="left:370px;top:570px;width:138px;height:100px;background:linear-gradient(135deg,#2f5fb0,#e8d43a)"></div>

    <p class="legal" style="top:686px">* Alle angegebenen Preise verstehen sich in Euro zzgl. der gesetzlichen geltenden Mehrwertsteuer von derzeit 19%.<br>Die Lieferung erfolgt ca.10 Tage nach Bestelleingang. Porto/Verpackung 8,90 Euro</p>
    <p class="imprint" style="top:716px">Fördergesellschaft Klever Technik mbH · Lindenweg 12 · 80331 München · www.klvt.de</p>
  </section>

</div>
</body>
</html>
```